New Company Business Card Design

I have a new company logo and I want a new business card design. I dont know if the logo file i attached is in the correct format or quality. We are a New York City Specialty construction Firm specializing in high risk out of the box projects. I want a simple and classy business card that people will his card is as crisp as the work his company does.

Target Market(s)

Clients in the heavy construction industry in New York City

Industry/Entity Type

Construction Company

Contact Information for Business Card

Simple Classy - DIFFERENT

Font styles to use
Other font styles liked:
• Mach the logo font in some way

Colors

Designer to choose colors to be used in the design.

Requirements
Must have
• Uniqueness
Nice to have
• Nothing particular - Just different and classy - Timeless
Should not have
• Goofy Shit or Gimmicky shit

```html
<!DOCTYPE html>
<html lang="en">
<head>
<meta charset="utf-8">
<title>KRT Builders, Inc. — Business Card</title>
<link href="https://fonts.googleapis.com/css2?family=Arimo:wght@400;700&family=Archivo+Black&display=swap" rel="stylesheet">
<style>
  :root {
    --page-bg: #e4e2de;
    --card-dark: #29292b;
    --card-band: #3b3b3e;
    --ghost-letters: #56565a;
    --map-tone: #343437;
    --brand-blue: #1d8bd3;
    --text-light: #f2f2f2;
    --text-muted: #d6d6d6;
  }
  * { margin: 0; padding: 0; box-sizing: border-box; }
  html, body {
    width: 1200px; height: 900px; overflow: hidden;
    background: var(--page-bg);
    font-family: "Arimo", Arial, sans-serif;
  }
  .canvas {
    width: 1200px; height: 900px;
    display: flex; flex-direction: column;
    align-items: center; justify-content: center; gap: 40px;
  }
  .card {
    width: 630px; height: 360px;
    position: relative; overflow: hidden;
    background: var(--card-dark);
    box-shadow: 0 10px 28px rgba(0,0,0,0.28);
  }

  /* Back side */
  .card-back .world-map {
    position: absolute; inset: 24px 30px;
    background: radial-gradient(ellipse at 50% 45%, #3a3a3d 0%, var(--map-tone) 55%, var(--card-dark) 100%);
    border-radius: 40% / 50%;
  }
  .brand-lockup {
    position: absolute; left: 50%; top: 50%;
    transform: translate(-50%, -50%);
    display: flex; align-items: center; gap: 16px;
  }
  .brand-dot {
    width: 22px; height: 22px; border-radius: 50%;
    background: var(--brand-blue);
  }
  .brand-name {
    font-weight: 700; font-size: 40px; letter-spacing: 3px;
    color: var(--brand-blue); white-space: nowrap;
  }

  /* Front side */
  .card-front .top-band {
    position: absolute; left: 0; top: 0; width: 100%; height: 170px;
    background: var(--card-band);
  }
  .ghost-mark {
    position: absolute; left: -6px; top: -14px;
    font-family: "Archivo Black", "Arial Black", sans-serif;
    font-size: 250px; line-height: 1; letter-spacing: -4px;
    color: var(--ghost-letters);
  }
  .holder {
    position: absolute; right: 22px; top: 52px; text-align: right;
  }
  .holder-name {
    font-weight: 700; font-size: 38px; color: var(--brand-blue);
    letter-spacing: 0.5px; white-space: nowrap;
  }
  .holder-title {
    font-size: 15px; color: var(--text-light); margin-top: 4px; letter-spacing: 0.5px;
  }
  .contact-row {
    position: absolute; left: 0; right: 0; top: 200px;
    display: grid; grid-template-columns: 1fr 1fr 1fr;
  }
  .contact-item {
    display: flex; flex-direction: column; align-items: center;
    font-weight: 700; font-size: 15px; line-height: 1.3;
    color: var(--text-light); text-align: center;
  }
  .contact-icon { width: 40px; height: 40px; margin-bottom: 14px; }
  .contact-item:nth-child(2) { padding-top: 14px; }
  .contact-item:nth-child(3) { padding-top: 22px; }
</style>
</head>
<body>
<main class="canvas">

  <section class="card card-back" aria-label="Card back">
    <div class="world-map" role="img" aria-label="Faint world map background"></div>
    <div class="brand-lockup">
      <span class="brand-dot"></span>
      <span class="brand-name">KRT BUILDERS, INC.</span>
    </div>
  </section>

  <section class="card card-front" aria-label="Card front">
    <div class="top-band"></div>
    <div class="ghost-mark" aria-hidden="true">KRT</div>
    <div class="holder">
      <p class="holder-name">Marcus T. Rinaldi</p>
      <p class="holder-title">CEO | Founder</p>
    </div>

    <div class="contact-row">
      <div class="contact-item">
        <svg class="contact-icon" viewBox="0 0 40 40" aria-hidden="true">
          <circle cx="20" cy="20" r="18" fill="none" stroke="var(--brand-blue)" stroke-width="2"/>
          <path d="M14 12c1-1 2-1 3 0l2 3c.5 1 0 2-1 2.5 1 2.5 2.5 4 5 5 .5-1 1.5-1.5 2.5-1l3 2c1 1 1 2 0 3-3 3-8 1-11.5-2.5S11 15 14 12z" fill="var(--brand-blue)"/>
        </svg>
        <span>201-555-0148 (Off.)</span>
        <span>646-555-0192 (Cell)</span>
      </div>
      <div class="contact-item">
        <svg class="contact-icon" viewBox="0 0 40 40" aria-hidden="true">
          <circle cx="20" cy="20" r="18" fill="none" stroke="var(--brand-blue)" stroke-width="2"/>
          <g fill="none" stroke="var(--brand-blue)" stroke-width="1.6">
            <circle cx="20" cy="20" r="9"/>
            <ellipse cx="20" cy="20" rx="4" ry="9"/>
            <line x1="11" y1="20" x2="29" y2="20"/>
            <line x1="12.5" y1="15.5" x2="27.5" y2="15.5"/>
            <line x1="12.5" y1="24.5" x2="27.5" y2="24.5"/>
          </g>
        </svg>
        <span>marcus@krtbuild.com</span>
        <span>www.krtbuild.com</span>
      </div>
      <div class="contact-item">
        <svg class="contact-icon" viewBox="0 0 40 40" aria-hidden="true">
          <circle cx="20" cy="20" r="18" fill="none" stroke="var(--brand-blue)" stroke-width="2"/>
          <path d="M20 10a6.5 6.5 0 0 0-6.5 6.5c0 5 6.5 13 6.5 13s6.5-8 6.5-13A6.5 6.5 0 0 0 20 10z" fill="none" stroke="var(--brand-blue)" stroke-width="2"/>
          <circle cx="20" cy="16.5" r="2.3" fill="var(--brand-blue)"/>
        </svg>
        <span>128 Harbor Point Road-</span>
        <span>Linden,</span>
        <span>New Jersey 07036</span>
      </div>
    </div>
  </section>

</main>
</body>
</html>
```